OLUM Sign
OLUM leasing sign
#12 I'd like to go with this design with a few minor changes. Could you please change the font of Daniel Pruett to something that works better with the other font Office space? and can you remove the rectangles under the phone number? I promise i'll respond more quickly once i see the revisions.
additional comment on 23 -24. I think I like these for their clean simplicity (although they need the required information and the proper logo)
#23 ,#24 These looks different - good. Can you try a grey background, with correct logo (maybe in white). There is now an .eps file available. The sign must have phone number, "Office Space", and Realtor's name. use only the colors in logo, and black.
Dear PH, thanks for your valuable feedback.Will submit some more design options...regards,
will upload vector file. these designs are not what we are looking for. we want an eye catching creative design that doesn't look like a typical leasing sign.
Dear PH, Can you please upload the vector file (.ai or .eps) of the logo.Regards.

```html
<!DOCTYPE html>
<html lang="en">
<head>
<meta charset="utf-8">
<title>OLUM Leasing Sign</title>
<link rel="stylesheet" href="https://fonts.googleapis.com/css2?family=Archivo+Black&family=Archivo:wght@400;800;900&display=swap">
<style>
  :root {
    --sign-red: #d9141b;
    --sign-white: #ffffff;
    --logo-grey: #8a8c8f;
    --backdrop: #eceeef;
  }
  * { margin: 0; padding: 0; box-sizing: border-box; }
  html, body {
    width: 1200px;
    height: 901px;
    overflow: hidden;
    background: var(--backdrop);
  }
  .canvas {
    position: relative;
    width: 1200px;
    height: 901px;
  }
  .sign {
    position: absolute;
    left: 170px;
    top: 74px;
    width: 860px;
    height: 752px;
    background: var(--sign-white);
    overflow: hidden;
    box-shadow: 0 6px 24px rgba(0,0,0,0.18);
  }
  .sign__bands {
    position: absolute;
    inset: 0;
  }
  .headline {
    position: absolute;
    left: 0;
    width: 100%;
    text-align: center;
    font-family: "Archivo Black", "Arial Black", sans-serif;
    color: var(--sign-white);
    -webkit-text-stroke: 14px var(--sign-red);
    paint-order: stroke fill;
    line-height: 1;
    white-space: nowrap;
  }
  .headline--available {
    top: 16px;
    font-size: 96px;
    letter-spacing: -1px;
  }
  .headline--space {
    top: 148px;
    font-size: 92px;
    letter-spacing: -3px;
    transform: scaleX(0.9);
  }
  .agent {
    position: absolute;
    left: 0;
    width: 100%;
    text-align: center;
    font-family: "Archivo", "Arial", sans-serif;
    font-weight: 900;
    color: var(--sign-red);
    line-height: 1;
    white-space: nowrap;
  }
  .agent__name {
    top: 332px;
    font-size: 80px;
    letter-spacing: -1px;
  }
  .agent__phone {
    top: 440px;
    font-size: 68px;
    font-weight: 800;
  }
  .brand {
    position: absolute;
    left: 0;
    top: 566px;
    width: 100%;
    text-align: center;
    font-family: "Archivo", "Arial", sans-serif;
    color: var(--logo-grey);
    line-height: 1;
  }
  .brand__name {
    display: block;
    font-size: 96px;
    font-weight: 900;
    letter-spacing: 2px;
  }
  .brand__tag {
    display: block;
    margin-top: 8px;
    font-size: 24px;
    font-weight: 900;
    letter-spacing: 3px;
  }
</style>
</head>
<body>
<main class="canvas">
  <section class="sign" aria-label="OLUM leasing sign">
    <svg class="sign__bands" viewBox="0 0 860 752" preserveAspectRatio="none" aria-hidden="true">
      <path d="M0 0 H58 Q30 376 50 752 H0 Z" fill="var(--sign-red)"/>
      <path d="M860 0 H800 Q832 376 812 752 H860 Z" fill="var(--sign-red)"/>
    </svg>

    <h1 class="headline headline--available">Available</h1>
    <h2 class="headline headline--space">OFFICE SPACE</h2>

    <p class="agent agent__name">Daniel Pruett</p>
    <p class="agent agent__phone">555-218-0473</p>

    <div class="brand">
      <span class="brand__name">OLUM</span>
      <span class="brand__tag">REALTY GROUP</span>
    </div>
  </section>
</main>
</body>
</html>
```